Web Design for Solar Energy Consultancy Company

~ May 3, 2017 Update ~
As our project is rapidly progressing towards its completion, we started building up the list of designs that attracted the most of the team's attention. Additional submittals are still most welcome. Before submitting your proposal, however, we can recommend to review the concepts that received 4 stars as these are the ones that, in our opinion, most closely match the brief's requirements. Thank you!!
~ April 30, 2017 Update ~
The project deadline has been extended to attract a broader design community and to better tailor the final design to the requirements of the project.
A "light", "clean" (minimalistic), professionally looking, unique design is expected. Please, try to avoid industry cliches. Also, please use green, which became another industry cliche, with great caution. The brief provides minimum details to foster creativity. With the same notion in mind, the page content information is not provided.
Thank you for your feedback and support of the project!!
~ April 22, 2017 Update ~
Additional comments after starting receiving more designs:
- your attention to the brief's requirements will be highly appreciated. It is expected that the design is unique - standard, commonly used, images, formats and approaches do not fall under this category. There is no need to "bombard" with slightly different variations of the same design. It is expected that a conceptual (preliminary) design is submitted first, and, after it is reviewed (each design will receive a star rating and, if the star rating is greater than 3, a detailed feedback), the requested changes are implemented. We believe this will allow to approach the design process more efficiently and safe additional time to both the Designers's Community and our company. Thank you for understanding.
Clarification, please submit two variations of a design:
1) 1 page "business card" design that the company will be able to use during its startup stage;
2) the fully functional design (as per the requirements outlined below) for the company to transition to after the start-up period is over. Same design principles as developed for option 1 should be used for this variation.
Additional clarification, please note that the news block will not require images (at least during the start-up stage). It is envisioned to be a news feeder.
~ April 21, 2017 Update ~
Preliminary comments after receiving first designs:
- please try to create a unique design, using common elements wisely. Though such solar energy "attributes" as a solar panel or a bulb are very well recognized and allow quickly identify the nature of the business, they also became so common that in many cases a design may seem very similar to the one of others (Oh!, I've already seen this... effect).
- please try to introduce the company's logo unobtrusively. The size and position of the logo should clearly identify the company, but the message should be subtle, the logo should not distract from the main design. Brevam's swoosh did not need to occupy have the screen.
- please use the green color with caution as it was with the company's logo. True, it is a green energy. But there is no need for the color to "scream" about it. Use the amount of green and its tone (avoid acid green) wisely.
--------------------------------------------------------------------------------
1. Main Goal
Develop a website that can represent the company to the industry stakeholders and become its "business card" during the start-up stage.
2. Secondary Goal
Develop a structure of a fully functional website that the "business card" design can eventually be transformed to staying consistent with the original design principles.
3. Key Audience
Varlo Corp. is providing consulting and technical services in the area of Solar Energy. The industry stakeholders include project developers, financial community, governmental bodies, OEMs, and competition.
4. Site Map
- HOME
• About
• Services
• Solar Energy
• News
• Contacts
• Social Media
- SERVICES*
- PROJECTS*
- FINANCE*
- TRAINING*
- SOLAR (ENERGY)*
* Maybe inactive / partially functional during the start-up stage.
5. Technical Specifications
Online brochure website during the start-up stage with a capability to be eventually transformed to a fully functional website while preserving the original design principles.
The design to be appealing, "light", professional, and with an intuitive and easy to navigate interface. Modern coding principles supporting efficiency and security to be utilized. Newest industry trends in website coding will be welcome.
The website to be designed so that it would fit well a computer, tablet, or mobile phone screen of any size. Cross-platform functionality to be taken into consideration to ensure that the website is fully functional on any platform.
Company's logo has already been designed and will be shared with the short-listed designers during the final design stage.
6. Interaction
The website will provide information about the company, our services, and projects. In addition, the industry insight, accumulated knowledge, and most recent trends are planned to be shared with stakeholders and attract and retain the audience.
Interaction with designers during the website development is envisioned to go through the following steps:
a) conceptual design - to be proposed by a designer originally. All conceptual designs will be reviewed and a feedback provided to pre-selected designers;
b) (preliminary and) final design - depending on the level of additional changes required can be broken into two steps. After discussing preliminary designs, company images will be provided to the selected finalists, who will compete with their final proposals.
7. Industry Stakeholders
- https://www.quelbrant.example/power/solar-power.- http://www.tavlorpeak.example/
- http://www.morvexaworks.example/about/company/
- https://www.pyxbel.example/energy/index.html
8. Budget
Defined by the project.
9. Timescale
Defined by the project.
12. Additional Info
- No copy-cats, standard graphics, or cliches please!
- Additional information / clarifications will be gladly provided upon request.
- This specification may be updated throughout the project to reflect discussions with / changes proposed by the Designers community.
Updates

```html
<!DOCTYPE html>
<html lang="en">
<head>
<meta charset="utf-8">
<title>Varlo Corp. — Solar Energy Consulting</title>
<link rel="stylesheet" href="https://fonts.googleapis.com/css2?family=Open+Sans:wght@400;600;700&family=Poppins:wght@400;500;600&display=swap">
<style>
:root{
  --orange:#f5a01a;
  --dark:#222222;
  --footer:#1e1e1e;
  --footer-bottom:#111111;
  --ink:#333333;
  --muted:#9a9a9a;
  --green:#3a9a3a;
  --white:#ffffff;
  --tile:#d6d6d6;
}
*{box-sizing:border-box;margin:0;padding:0}
html,body{width:1200px;height:2990px;overflow:hidden}
body{font-family:"Open Sans",Arial,sans-serif;color:var(--ink);background:var(--white);position:relative}
.abs{position:absolute}

/* top bar */
.topbar{left:0;top:0;width:1200px;height:36px;background:var(--dark);color:#ddd;font-size:11px;display:flex;align-items:center;justify-content:space-between;padding:0 58px}
.topbar .hours{display:flex;align-items:center;gap:8px}
.topbar .follow{display:flex;align-items:center;gap:14px}
.dot-s{width:8px;height:8px;border-radius:50%;background:#ddd;display:inline-block}

/* header */
.header{left:0;top:36px;width:1200px;height:110px}
.brand{position:absolute;left:56px;top:14px;display:flex;align-items:center;gap:14px}
.brand-mark{width:80px;height:80px;border-radius:50%;background:var(--orange)}
.brand-name{font-size:42px;font-weight:700;color:#444;letter-spacing:2px}
.contact{position:absolute;top:24px;display:flex;align-items:center;gap:14px;white-space:nowrap}
.contact .ring{width:52px;height:52px;border:3px solid var(--green);border-radius:50%;display:flex;align-items:center;justify-content:center;flex:none}
.contact .label{font-size:17px;color:#555}
.contact .value{font-size:25px;font-weight:600;color:#444;line-height:1.2}

/* nav */
.nav{left:0;top:146px;width:1200px;height:50px;background:var(--orange);display:flex;align-items:center;padding:0 56px;gap:38px;color:var(--white);font-size:15px;font-weight:600}
.nav .search{margin-left:auto}

/* hero */
.hero{left:0;top:196px;width:1200px;height:394px;background:linear-gradient(180deg,#7a6a55 0%,#5a5048 45%,#2f3540 75%,#3a4352 100%)}
.hero h1{position:absolute;left:54px;top:92px;color:var(--white);font-size:54px;font-weight:600;line-height:62px;letter-spacing:1px}
.btn-light{position:absolute;left:56px;top:262px;width:158px;height:42px;background:var(--white);color:#222;font-size:17px;font-weight:600;display:flex;align-items:center;justify-content:center}
.dots{display:flex;gap:10px}
.dots span{width:9px;height:9px;border-radius:50%;background:#aaa}
.dots span.on{background:#fff}
.hero .dots{position:absolute;left:572px;top:364px}

/* about */
.about-title{left:58px;top:636px;font-size:34px;font-weight:600;color:#333}
.about-text{left:56px;top:702px;width:574px;font-size:16px;line-height:21.5px;color:var(--muted)}
.about-text p+p{margin-top:22px}
.about-img{left:740px;top:676px;width:400px;height:234px;background:linear-gradient(135deg,#3a5fb0,#1c2f6a 60%,#2a2a2a)}

/* services */
.services{left:0;top:970px;width:1200px;height:636px;background:linear-gradient(90deg,#8a8a8a 0%,#6c6c6c 55%,#5a5a5a 100%)}
.services-photo{position:absolute;left:0;top:0;width:620px;height:636px;background:radial-gradient(circle at 55% 50%,#e8c22a 0%,#c9a21c 30%,#8a8478 60%,#7a7a7a 100%)}
.services h2{position:absolute;left:612px;top:62px;color:var(--white);font-size:34px;font-weight:600}
.services .intro{position:absolute;left:612px;top:134px;width:470px;color:#eee;font-size:12px;line-height:20px}
.tiles{position:absolute;left:612px;top:222px;display:grid;grid-template-columns:repeat(3,144px);grid-auto-rows:144px;column-gap:25px;row-gap:26px}
.tile{background:var(--tile);padding:26px 0 0 26px;color:#333;font-size:11.5px;font-weight:600;line-height:20px;text-transform:uppercase}
.tile svg{display:block;margin-bottom:14px}

/* projects */
.section-title{width:1200px;text-align:center;font-size:34px;font-weight:600;color:#333}
.projects-sub{left:0;top:1700px;width:1200px;text-align:center;font-size:14px;color:#444}
.rule{left:580px;top:1752px;width:40px;height:2px;background:var(--orange)}
.project{position:absolute;top:1802px;width:252px}
.project .ph{height:202px}
.project .cap{margin-top:32px;text-align:center;font-family:"Poppins",sans-serif;font-weight:500;font-size:17px;color:#222}
.projects-dots{position:absolute;left:574px;top:2080px}
.projects-dots span{background:#bbb}
.projects-dots span.on{background:#666}

/* news */
.news{left:0;top:2136px;width:1200px;height:514px;background:linear-gradient(135deg,#f2f2f2,#e6e9ec 50%,#eef0f2)}
.news .section-title{position:absolute;left:0;top:40px}
.news-item{position:absolute;display:flex;gap:18px}
.news-item .thumb{width:108px;height:108px;background:linear-gradient(135deg,#9bb0c8,#3e5a86)}
.news-item .date{display:flex;align-items:center;gap:8px;font-size:13px;color:#444;margin-top:8px}
.news-item .title{font-size:21px;color:#444;margin-top:8px}
.news-item .more{font-size:21px;color:var(--green);margin-top:2px}

/* footer */
.footer{left:0;top:2650px;width:1200px;height:294px;background:var(--footer);color:var(--white)}
.footer h4{font-size:13px;font-weight:700;margin-bottom:28px}
.fcol{position:absolute;top:38px}
.fline{display:flex;gap:16px;font-size:12px;line-height:17px;margin-bottom:26px}
.links{list-style:none;font-size:12px;line-height:27px}
.news-form p{font-size:12px;line-height:22px;width:240px}
.news-form .field{margin-top:12px;width:226px;height:34px;background:var(--white);color:#333;font-size:12px;padding:9px 6px}
.news-form .sub{margin-top:18px;width:226px;height:34px;background:var(--orange);font-size:12px;display:flex;align-items:center;justify-content:center}
.social{display:flex;gap:14px}
.social span{width:16px;height:16px;border-radius:50%;background:#ddd}
.social span:first-child{background:var(--orange)}
.copy{left:0;top:2944px;width:1200px;height:46px;background:var(--footer-bottom);color:#ccc;font-size:12px;display:flex;align-items:center;justify-content:center}
</style>
</head>
<body>

<div class="abs topbar">
  <div class="hours">
    <svg width="12" height="12" viewBox="0 0 12 12"><circle cx="6" cy="6" r="5" fill="none" stroke="#ddd" stroke-width="1.3"/><path d="M6 3v3l2 1.5" fill="none" stroke="#ddd" stroke-width="1.3"/></svg>
    Opening Times: Mon - Sat 8.00 - 18.00
  </div>
  <div class="follow">Follow us: <span class="dot-s"></span><span class="dot-s"></span><span class="dot-s"></span><span class="dot-s"></span></div>
</div>

<header class="abs header">
  <div class="brand"><span class="brand-mark"></span><span class="brand-name">VARLO CORP.</span></div>
  <div class="contact" style="left:594px">
    <div class="ring"><svg width="24" height="24" viewBox="0 0 24 24"><path d="M6 3l3 0 2 5-2 1.5c1 2.5 3 4.5 5.5 5.5L16 13l5 2v3c0 1-1 2-2 2C10 20 4 14 4 5c0-1 1-2 2-2z" fill="var(--green)"/></svg></div>
    <div><div class="label">Call us:</div><div class="value">2265550148</div></div>
  </div>
  <div class="contact" style="left:852px">
    <div class="ring"><svg width="24" height="20" viewBox="0 0 24 20"><rect x="2" y="3" width="20" height="14" rx="1" fill="var(--green)"/><path d="M3 4l9 7 9-7" fill="none" stroke="#fff" stroke-width="1.6"/></svg></div>
    <div><div class="label">Email :</div><div class="value">lorem@varlo.example</div></div>
  </div>
</header>

<nav class="abs nav">
  <span>HOME &nbsp;▾</span><span>SERVICES</span><span>PROJECTS</span><span>FINANCE</span><span>TRAINING</span><span>SOLAR (ENERGY)</span>
  <svg class="search" width="22" height="22" viewBox="0 0 22 22"><circle cx="9" cy="9" r="7" fill="none" stroke="#fff" stroke-width="2.4"/><path d="M14 14l6 6" stroke="#fff" stroke-width="2.6"/></svg>
</nav>

<section class="abs hero" role="img" aria-label="Solar panel field in front of a city skyline at sunset with wind turbines">
  <h1>Lorem ipsum dolor<br>sit amet consect</h1>
  <div class="btn-light">Learn More</div>
  <div class="dots"><span></span><span class="on"></span><span></span></div>
</section>

<h2 class="abs about-title">About Varlo Corp.</h2>
<div class="abs about-text">
  <p>Lorem ipsum dolor sit amet, consectetur adipisicing elit, sed do eius-mod tempor incididunt ut labore et dolore magna aliqua. Ut enim ad minim veniam, quis nostrud exercitation ullamco laboris nisi ut aliquip ex ea commodo consequat. Duis aute irure dolor in reprehenderit in voluptate velit esse cillum dolore eu fugiat nulla pariatur. Excepteur sint occaecat</p>
  <p>na aliqua. Ut enim ad minim veniam, quis nostrud exercitation ullamco laboris nisi ut aliquip ex ea commodo consequat te irure dolor in reprehenderit.</p>
</div>
<div class="abs about-img" role="img" aria-label="Tilted solar panel array on a mounting frame"></div>

<section class="abs services">
  <div class="services-photo" role="img" aria-label="Gloved hand holding a yellow hard hat"></div>
  <h2>Our Services</h2>
  <p class="intro">Lorem ipsum dolor sit amet, consectetur adipiscing elit. Curabitur vitae arcu nec metus ultrices scelerisque facilisis id leo. Praesent iaculis lorem ut dictum tempus. Pellentesque sit amet erat at orci bibendum consequat.</p>
  <div class="tiles">
    <div class="tile"><svg width="26" height="30" viewBox="0 0 26 30" fill="none" stroke="#333" stroke-width="1.4"><path d="M13 3a8 8 0 0 0-5 14v4h10v-4a8 8 0 0 0-5-14z"/><path d="M9 24h8M10 27h6"/></svg>Development<br>Ideas</div>
    <div class="tile"><svg width="26" height="30" viewBox="0 0 26 30" fill="none" stroke="#333" stroke-width="1.4"><path d="M20 4a5 5 0 0 0-5 7L4 22l3 3 11-11a5 5 0 0 0 7-5l-3 3-3-1-1-3z"/></svg>Technical<br>Development</div>
    <div class="tile"><svg width="26" height="30" viewBox="0 0 26 30" fill="none" stroke="#333" stroke-width="1.4"><circle cx="13" cy="14" r="4"/><circle cx="13" cy="14" r="9" stroke-dasharray="4 3"/></svg>Realization<br>of Projects</div>
    <div class="tile"><svg width="26" height="30" viewBox="0 0 26 30" fill="none" stroke="#333" stroke-width="1.4"><path d="M3 11h5l10-6v18l-10-6H3z"/><path d="M6 17l2 7h3l-1-7M21 11h3M21 15h3"/></svg>Projects<br>Advertising</div>
    <div class="tile"><svg width="26" height="30" viewBox="0 0 26 30" fill="none" stroke="#333" stroke-width="1.4"><path d="M13 12V29M13 12L13 2M13 12L4 17M13 12l9 5"/></svg>Projects<br>Installation</div>
    <div class="tile"><svg width="30" height="30" viewBox="0 0 30 30" fill="none" stroke="#333" stroke-width="1.4"><circle cx="8" cy="18" r="5"/><circle cx="22" cy="18" r="5"/><path d="M13 18h4M3 18L6 6M27 18L24 6"/></svg>Technical<br>Support</div>
  </div>
</section>

<h2 class="abs section-title" style="left:0;top:1640px">Our Latest Projects</h2>
<p class="abs projects-sub">Lorem ipsum dolor sit amet, consectetur adipisicing elit. Et culpa dolore odio voluptate suscipit corporis sed ad sunt autem!</p>
<div class="abs rule"></div>
<div class="project" style="left:54px"><div class="ph" role="img" aria-label="Workers installing solar panels on a tiled roof" style="background:linear-gradient(135deg,#9a6a4a,#5e6c8a)"></div><div class="cap">Harlow House</div></div>
<div class="project" style="left:334px"><div class="ph" role="img" aria-label="Large solar panel arrays under a blue sky" style="background:linear-gradient(160deg,#8fbde8,#2c4f8e)"></div><div class="cap">Texas Industry</div></div>
<div class="project" style="left:616px"><div class="ph" role="img" aria-label="Rows of solar panels against a bright sky" style="background:linear-gradient(160deg,#bcd6ee,#1d2f60)"></div><div class="cap">Salt Lack City</div></div>
<div class="project" style="left:896px"><div class="ph" role="img" aria-label="Solar mirror dish in a desert landscape" style="background:linear-gradient(180deg,#3c6fb8,#7a8aa0 60%,#c0603a)"></div><div class="cap">Corvel Television</div></div>
<div class="dots projects-dots"><span></span><span class="on"></span><span></span></div>

<section class="abs news" role="img" aria-label="Faded background of a worker installing solar panels">
  <h2 class="section-title">Company News</h2>
  <div class="news-item" style="left:54px;top:136px"><div class="thumb" role="img" aria-label="Solar panels on a roof"></div><div><div class="date"><svg width="14" height="14" viewBox="0 0 14 14" fill="none" stroke="#555"><rect x="1.5" y="2.5" width="11" height="10"/><path d="M1.5 5.5h11"/></svg>APL 22, 2018</div><div class="title">Etiam non neque ac odio consequat</div><div class="more">&nbsp;Read More</div></div></div>
  <div class="news-item" style="left:646px;top:136px"><div class="thumb" role="img" aria-label="Engineer standing by solar panels"></div><div><div class="date"><svg width="14" height="14" viewBox="0 0 14 14" fill="none" stroke="#555"><rect x="1.5" y="2.5" width="11" height="10"/><path d="M1.5 5.5h11"/></svg>APL 22, 2018</div><div class="title">Etiam non neque ac odio consequat</div><div class="more">&nbsp;Read More</div></div></div>
  <div class="news-item" style="left:54px;top:304px"><div class="thumb" role="img" aria-label="Technician working on rooftop panels"></div><div><div class="date" style="padding-left:22px">APL 22, 2018</div><div class="title">Etiam non neque ac odio consequat</div><div class="more">&nbsp;Read More</div></div></div>
  <div class="news-item" style="left:646px;top:304px"><div class="thumb" role="img" aria-label="Installer fitting a solar panel"></div><div><div class="date" style="padding-left:22px">APL 22, 2018</div><div class="title">Etiam non neque ac odio consequat</div><div class="more">&nbsp;Read More</div></div></div>
</section>

<footer class="abs footer">
  <div class="fcol" style="left:56px">
    <h4>CONTACTS</h4>
    <div class="fline"><svg width="10" height="14" viewBox="0 0 10 14"><path d="M5 0a5 5 0 0 0-5 5c0 4 5 9 5 9s5-5 5-9a5 5 0 0 0-5-5z" fill="#fff"/><circle cx="5" cy="5" r="2" fill="#1e1e1e"/></svg><span>418 W. Marren Ave, Suite B<br>Calden, New Jersey 07099</span></div>
    <div class="fline" style="margin-top:34px"><svg width="12" height="12" viewBox="0 0 24 24"><path d="M6 3h3l2 5-2 1.5c1 2.5 3 4.5 5.5 5.5L16 13l5 2v3c0 1-1 2-2 2C10 20 4 14 4 5c0-1 1-2 2-2z" fill="#fff"/></svg><span>1-800-555-0134</span></div>
    <div class="fline" style="margin-top:34px"><svg width="12" height="12" viewBox="0 0 12 12"><rect x="1" y="4" width="10" height="7" fill="#fff"/><rect x="3" y="1" width="6" height="3" fill="#fff"/></svg><span>1-908-555-0175</span></div>
  </div>
  <div class="fcol" style="left:384px">
    <h4>QUICK LINKS</h4>
    <ul class="links"><li>HOME</li><li>SERVICES</li><li>PROJECTS</li><li>FINANCE</li><li>TRAINING</li><li>SOLAR (ENERGY)</li></ul>
  </div>
  <div class="fcol news-form" style="left:632px">
    <h4 style="padding-left:2px">NEWSLETTER</h4>
    <p>Enter your e-mail and subscribe to our newsletter</p>
    <div class="field">E - mail</div>
    <div class="sub">SUBSCRIBE</div>
  </div>
  <div class="fcol" style="left:968px">
    <h4>FOLLOW US</h4>
    <div class="social"><span></span><span></span><span></span><span></span><span></span><span></span></div>
  </div>
</footer>
<div class="abs copy">Copyright © . All Rights Reserved</div>

</body>
</html>
```